International gym review site. Needs a full website frontend (mobile + desktop) designing and a logo

Our UK based business 'LiftHarbor' is launching its international review website for independent and hotel gyms. Our website will be a fresh, funky and clean version of Wanderquill but for gyms.
We require the designs in sketch, psd, illustrator

We would like to see clean designs that incorporate gym style icons. We also require our logo designing which will need to complement the design of the site. We have included wireframes of how we envisage the site coming together. However, we are very flexible on this and have nothing set in stone.

We would like the designs to mobile first focused with desktop experince being the latter (although we have wireframed for desktop - we are very open to ideas and suggestions)

Please find below a number of websites that we like and have found inspiration from:

- https://www.bookvane.example/uk/
- chatterloom.example
- Map is cool on here https://bigroster.bypilotcraft.example/
- Looks cool like nest n'go (listing section could be smaller) -https://tintforge.example/demos/themes/?product=rowable
- Like this but needs to be more compact https://rowkit-demos.brimfold.example/rentals/listing/private-bedroom-w-bathroom/
- Like the homepage of this one https://rankhop.venmora.example/
- https://www.paddlo.example.co.uk/hotels - looks clean, like the layout of this especially the hotel section
- https://www.paddlo.example.co.uk/Barcelona-Hotels.48213.hotel.ksp - the good to know section is good
- https://chipwire.example/2017/10/20/flickcast-unveils-a-suite-of-new-tools-to-help-creators-grow-their-channels-and-make-money/
- https://www.quietlodging.example/
- https://www.wheelmarket.example.co.uk

Target Market(s)

Fitness users and hotel goers who want to use a gym. Generally affluent aged 20-50years old of multi-nationalities

Industry/Entity Type

Fitness

Logo Text

LiftHarbor (optional)

Number of Pages Required

5+ page

Colors

Designer to choose colors to be used in the design.

Requirements
Must have
• Clean, flat minimal, pleasing on the eye.
• Bright / colourful
• Clean fonts (no specific font picked, will leave colour palette and fonts to the designer)
Should not have
• Cluttered and disorganised feel.
• Dark and dreary.

```html
<!DOCTYPE html>
<html lang="en">
<head>
<meta charset="utf-8">
<title>LiftHarbor – Barcelona</title>
<link href="https://fonts.googleapis.com/css2?family=Roboto:wght@400;500;700&family=Lato:wght@400;700&display=swap" rel="stylesheet">
<style>
:root{
  --blue:#0a8fd8;
  --blue-dark:#0677c2;
  --orange:#f7941d;
  --orange-deep:#f26f0f;
  --cyan:#15c9e6;
  --cyan-light:#5fe4f7;
  --ink:#1c1c1c;
  --text:#333;
  --grey-band:#efeff2;
  --star:#f5c518;
  --footer:#050505;
  --white:#fff;
}
*{box-sizing:border-box;margin:0;padding:0}
html,body{width:1200px;height:3905px;overflow:hidden}
body{font-family:"Lato",sans-serif;color:var(--text);background:var(--white);position:relative}
h1,h2,h3,.brand,.nav a,.btn{font-family:"Roboto",sans-serif}

.site-header{height:117px;display:flex;align-items:center;justify-content:space-between;padding:0 90px;background:var(--white);box-shadow:0 3px 10px rgba(0,0,0,.18);position:relative;z-index:3}
.brand{display:flex;align-items:center;gap:12px;font-weight:700;font-size:28px;color:var(--ink);letter-spacing:.5px}
.brand-dot{width:40px;height:40px;border-radius:50%;background:var(--blue)}
.nav{display:flex}
.nav a{font-size:15px;font-weight:500;color:var(--ink);text-decoration:none;margin-left:44px}

.hero{height:508px;position:relative}
.hero-map{position:absolute;inset:0;background:linear-gradient(135deg,#eceadf 0%,#e4e9dd 35%,#dde6e9 70%,#b9d8ec 100%)}
.city-card{position:absolute;left:390px;top:370px;width:420px;height:325px;background:var(--blue);color:var(--white);text-align:center;padding:0 48px;z-index:2}
.city-photo{position:absolute;left:119px;top:-89px;width:182px;height:182px;border-radius:50%;border:5px solid var(--white);background:linear-gradient(180deg,#6f86b8 0%,#a88f8b 60%,#6a5a52 100%)}
.city-card h2{margin-top:114px;font-size:28px;font-weight:500;letter-spacing:1px}
.city-card .stars{color:var(--star);font-size:16px;letter-spacing:3px;margin-top:6px}
.city-card p{font-size:13.5px;line-height:23px;margin-top:14px}

.band{position:relative;text-align:center}
.band h2{font-size:31px;font-weight:700;color:var(--ink);letter-spacing:.3px}
.band.grey{background:var(--grey-band)}
.featured{height:685px;padding-top:262px}
.hotel{height:638px;padding-top:72px}
.independent{height:646px;padding-top:72px}

.cards{display:flex;gap:30px;justify-content:center;text-align:left}
.band h2 + .cards{margin-top:24px}
.card{width:320px}
.card-photo{height:212px;border:6px solid var(--white);box-shadow:0 0 0 1px #cfcfcf,0 2px 6px rgba(0,0,0,.25)}
.card-head{display:flex;justify-content:space-between;align-items:center;margin-top:18px}
.card-head h3{font-size:17px;font-weight:700;color:var(--ink)}
.stars{color:var(--star);font-size:14px;letter-spacing:2px}
.card p{font-size:12.5px;line-height:22px;margin-top:12px;color:var(--ink);font-weight:700;padding-right:22px}
.btn{display:inline-block;width:205px;height:49px;line-height:49px;border-radius:25px;background:var(--blue);color:var(--white);font-size:15px;font-weight:500;text-align:center;text-decoration:none;position:absolute;right:89px;top:521px}

.stats{height:638px;padding-top:62px}
.charts{display:flex;gap:42px;justify-content:center;margin-top:42px}
.chart-card{width:463px;height:418px;background:var(--white);box-shadow:0 0 0 1px #dcdcdc,0 2px 6px rgba(0,0,0,.12)}
.chart-card h3{height:70px;line-height:70px;background:var(--orange);color:var(--white);font-family:"Lato",sans-serif;font-weight:400;font-size:21px;text-align:center}
.chart-card svg{display:block}

.events{height:341px;padding-top:74px}
.event-row{display:flex;gap:7px;justify-content:center;margin-top:22px}
.event{width:165px}
.event-photo{height:106px}
.event span{display:block;text-align:center;font-family:"Roboto",sans-serif;font-weight:700;font-size:14px;color:var(--ink);margin-top:12px}

.site-footer{position:absolute;left:0;top:3572px;width:1200px;height:333px;background:var(--footer);color:#ddd}
.foot-brand{position:absolute;left:92px;top:88px;font-size:34px;color:var(--white)}
.foot-brand .brand-dot{width:56px;height:56px}
.foot-col{position:absolute;top:46px}
.foot-col h4{font-family:"Lato",sans-serif;font-weight:400;font-size:15px;color:var(--white);margin-bottom:22px}
.info{left:416px}
.info ul,.links ul{list-style:none}
.info li{display:flex;gap:16px;font-size:12.5px;line-height:19px;margin-bottom:14px}
.info svg{flex:0 0 14px;margin-top:2px}
.links{left:677px}
.links li{font-size:11.5px;line-height:22px;font-family:"Roboto",sans-serif}
.links li::before{content:"›";margin-right:6px}
.signup{left:838px}
.signup .field{width:273px;height:52px;border:1px solid #bbb;font-size:11.5px;color:#bbb;padding:0 26px;line-height:50px}
.signup .submit{width:193px;height:50px;line-height:50px;margin-top:16px;background:var(--blue);color:var(--white);text-align:center;font-family:"Roboto",sans-serif;font-weight:500;font-size:14px}
.foot-rule{position:absolute;left:88px;right:88px;top:271px;border-top:1px solid #555}
.copyright{position:absolute;left:88px;top:292px;font-size:12px}
.social{position:absolute;right:88px;top:293px;display:flex;gap:18px}
.social i{width:12px;height:12px;border-radius:50%;background:#ddd;display:block}
</style>
</head>
<body>

<header class="site-header">
  <div class="brand"><span class="brand-dot"></span>LiftHarbor</div>
  <nav class="nav"><a href="#">HOME</a><a href="#">LISTINGS</a><a href="#">FEATURES</a><a href="#">PAGES</a><a href="#">LOG IN</a></nav>
</header>

<section class="hero">
  <div class="hero-map" role="img" aria-label="Street map of Barcelona with gym location clusters"></div>
  <div class="city-card">
    <div class="city-photo" role="img" aria-label="Barcelona skyline photo"></div>
    <h2>BARCELONA</h2>
    <div class="stars">★★★★★</div>
    <p>Lorem Ipsum is simply dummy text of the printing and typesetting industry. Lorem Ipsum has been the industry's standard dummy text ever since the 1500s, when an unknown printer took a galley of</p>
  </div>
</section>

<section class="band featured">
  <div class="cards">
    <article class="card"><div class="card-photo" role="img" aria-label="Athlete lifting a barbell in a gym" style="background:linear-gradient(180deg,#8d8a86,#4a4644)"></div><div class="card-head"><h3>BARCELONA</h3><span class="stars">★★★★★</span></div><p>Lorem Ipsum is simply dummy text of the printing and typesetting industry. Lorem Ipsum has been the industry's standard dummy text ever since the 1500s, when an unknown</p></article>
    <article class="card"><div class="card-photo" role="img" aria-label="Dark gym floor with weight machines" style="background:linear-gradient(180deg,#3a3c42,#6b4446)"></div><div class="card-head"><h3>BARCELONA</h3><span class="stars">★★★★★</span></div><p>Lorem Ipsum is simply dummy text of the printing and typesetting industry. Lorem Ipsum has been the industry's standard dummy text ever since the 1500s, when an unknown</p></article>
    <article class="card"><div class="card-photo" role="img" aria-label="Runner on a treadmill" style="background:linear-gradient(180deg,#5f6a74,#262a2f)"></div><div class="card-head"><h3>BARCELONA</h3><span class="stars">★★★★★</span></div><p>Lorem Ipsum is simply dummy text of the printing and typesetting industry. Lorem Ipsum has been the industry's standard dummy text ever since the 1500s, when an unknown</p></article>
  </div>
</section>

<section class="band grey hotel">
  <h2>HOTEL GYMS</h2>
  <div class="cards">
    <article class="card"><div class="card-photo" role="img" aria-label="Sunlit hotel gym with treadmills" style="background:linear-gradient(180deg,#e8b56a,#8a6a4a)"></div><div class="card-head"><h3>BARCELONA</h3><span class="stars">★★★★★</span></div><p>Lorem Ipsum is simply dummy text of the printing and typesetting industry. Lorem Ipsum has been the industry's standard dummy text ever since the 1500s, when an unknown</p></article>
    <article class="card"><div class="card-photo" role="img" aria-label="Woman training with dumbbells" style="background:linear-gradient(180deg,#b9a898,#4e4440)"></div><div class="card-head"><h3>BARCELONA</h3><span class="stars">★★★★★</span></div><p>Lorem Ipsum is simply dummy text of the printing and typesetting industry. Lorem Ipsum has been the industry's standard dummy text ever since the 1500s, when an unknown</p></article>
    <article class="card"><div class="card-photo" role="img" aria-label="Boxing studio with hanging bags" style="background:linear-gradient(180deg,#2a2a2a,#bfc3c6 55%,#2a2a2a)"></div><div class="card-head"><h3>BARCELONA</h3><span class="stars">★★★★★</span></div><p>Lorem Ipsum is simply dummy text of the printing and typesetting industry. Lorem Ipsum has been the industry's standard dummy text ever since the 1500s, when an unknown</p></article>
  </div>
  <a class="btn" href="#">VIEW MORE</a>
</section>

<section class="band independent">
  <h2>INDEPENDENT GYMS</h2>
  <div class="cards">
    <article class="card"><div class="card-photo" role="img" aria-label="Functional training space with a jumping athlete" style="background:linear-gradient(180deg,#8a7c70,#5a4a3e)"></div><div class="card-head"><h3>BARCELONA</h3><span class="stars">★★★★★</span></div><p>Lorem Ipsum is simply dummy text of the printing and typesetting industry. Lorem Ipsum has been the industry's standard dummy text ever since the 1500s, when an unknown</p></article>
    <article class="card"><div class="card-photo" role="img" aria-label="Athlete resting in a bright loft gym" style="background:linear-gradient(180deg,#d9dcdc,#5c6062)"></div><div class="card-head"><h3>BARCELONA</h3><span class="stars">★★★★★</span></div><p>Lorem Ipsum is simply dummy text of the printing and typesetting industry. Lorem Ipsum has been the industry's standard dummy text ever since the 1500s, when an unknown</p></article>
    <article class="card"><div class="card-photo" role="img" aria-label="Kettlebell workout on a gym floor" style="background:linear-gradient(180deg,#a89a92,#3b3634)"></div><div class="card-head"><h3>BARCELONA</h3><span class="stars">★★★★★</span></div><p>Lorem Ipsum is simply dummy text of the printing and typesetting industry. Lorem Ipsum has been the industry's standard dummy text ever since the 1500s, when an unknown</p></article>
  </div>
  <a class="btn" href="#">VIEW MORE</a>
</section>

<section class="band grey stats">
  <h2>WHAT IS NIGHTLY IN STATS?</h2>
  <div class="charts">
    <div class="chart-card">
      <h3>AVERAGE NIGHTLY PRICE PER MONTH</h3>
      <svg width="463" height="348" viewBox="0 0 463 348" font-family="Lato, sans-serif">
        <g font-size="11" fill="#777" text-anchor="end">
          <text x="52" y="90">$150</text><text x="52" y="114">$125</text><text x="52" y="138">$100</text><text x="52" y="162">$75</text><text x="52" y="186">$50</text><text x="52" y="210">$25</text><text x="52" y="234">$0</text>
        </g>
        <g stroke="#e6e6e6"><line x1="60" y1="86" x2="400" y2="86"/><line x1="60" y1="110" x2="400" y2="110"/><line x1="60" y1="134" x2="400" y2="134"/><line x1="60" y1="158" x2="400" y2="158"/><line x1="60" y1="182" x2="400" y2="182"/><line x1="60" y1="206" x2="400" y2="206"/><line x1="60" y1="230" x2="400" y2="230"/></g>
        <rect x="72" y="132" width="34" height="98" fill="#f26f0f"/>
        <rect x="150" y="150" width="34" height="80" fill="#f7941d"/>
        <rect x="232" y="70" width="34" height="160" fill="#5fe4f7"/>
        <rect x="314" y="166" width="34" height="64" fill="#15c9e6"/>
        <g font-size="17" fill="#555" text-anchor="middle"><text x="89" y="124">30%</text><text x="167" y="142">25%</text><text x="249" y="62">50%</text><text x="331" y="158">20%</text></g>
        <g font-size="11" fill="#777" text-anchor="middle"><text x="89" y="250">JAN</text><text x="167" y="250">FEB</text><text x="249" y="250">MAR</text><text x="331" y="250">APR</text></g>
        <g font-size="14" fill="#555">
          <rect x="26" y="286" width="12" height="12" fill="#f7941d"/><text x="46" y="297">Series 1</text>
          <rect x="132" y="286" width="12" height="12" fill="#15c9e6"/><text x="152" y="297">Series 2</text>
          <rect x="238" y="286" width="12" height="12" fill="#f26f0f"/><text x="258" y="297">Series 3</text>
          <rect x="344" y="286" width="12" height="12" fill="#5fe4f7"/><text x="364" y="297">Series 4</text>
        </g>
      </svg>
    </div>
    <div class="chart-card">
      <h3>AVERAGE NIGHTLY PRICE PER MONTH</h3>
      <svg width="463" height="348" viewBox="0 0 463 348" font-family="Lato, sans-serif">
        <g font-size="11" fill="#777" text-anchor="end">
          <text x="52" y="90">$150</text><text x="52" y="114">$125</text><text x="52" y="138">$100</text><text x="52" y="162">$75</text><text x="52" y="186">$50</text><text x="52" y="210">$25</text><text x="52" y="234">$0</text>
        </g>
        <g stroke="#e6e6e6"><line x1="60" y1="86" x2="400" y2="86"/><line x1="60" y1="110" x2="400" y2="110"/><line x1="60" y1="134" x2="400" y2="134"/><line x1="60" y1="158" x2="400" y2="158"/><line x1="60" y1="182" x2="400" y2="182"/><line x1="60" y1="206" x2="400" y2="206"/><line x1="60" y1="230" x2="400" y2="230"/></g>
        <rect x="72" y="132" width="34" height="98" fill="#f26f0f"/>
        <rect x="150" y="150" width="34" height="80" fill="#f7941d"/>
        <rect x="232" y="70" width="34" height="160" fill="#5fe4f7"/>
        <rect x="314" y="166" width="34" height="64" fill="#15c9e6"/>
        <g font-size="17" fill="#555" text-anchor="middle"><text x="89" y="124">30%</text><text x="167" y="142">25%</text><text x="249" y="62">50%</text><text x="331" y="158">20%</text></g>
        <g font-size="11" fill="#777" text-anchor="middle"><text x="89" y="250">JAN</text><text x="167" y="250">FEB</text><text x="249" y="250">MAR</text><text x="331" y="250">APR</text></g>
        <g font-size="14" fill="#555">
          <rect x="26" y="286" width="12" height="12" fill="#f7941d"/><text x="46" y="297">Series 1</text>
          <rect x="132" y="286" width="12" height="12" fill="#15c9e6"/><text x="152" y="297">Series 2</text>
          <rect x="238" y="286" width="12" height="12" fill="#f26f0f"/><text x="258" y="297">Series 3</text>
          <rect x="344" y="286" width="12" height="12" fill="#5fe4f7"/><text x="364" y="297">Series 4</text>
        </g>
      </svg>
    </div>
  </div>
</section>

<section class="band events">
  <h2>EVENTS NEAR BY</h2>
  <div class="event-row">
    <div class="event"><div class="event-photo" role="img" aria-label="Outdoor group stretching class" style="background:linear-gradient(180deg,#9fb3c4,#6d7a6a)"></div><span>EVENT 1</span></div>
    <div class="event"><div class="event-photo" role="img" aria-label="Group fitness session indoors" style="background:linear-gradient(180deg,#b07a52,#4a3a30)"></div><span>EVENT 2</span></div>
    <div class="event"><div class="event-photo" role="img" aria-label="Crowd at a fitness event" style="background:linear-gradient(180deg,#5d7a4c,#3a2e2e)"></div><span>BARCELONA</span></div>
    <div class="event"><div class="event-photo" role="img" aria-label="Athletes training in a large hall" style="background:linear-gradient(180deg,#c8ccd0,#6a6e72)"></div><span>BARCELONA</span></div>
    <div class="event"><div class="event-photo" role="img" aria-label="Gym with orange equipment" style="background:linear-gradient(180deg,#e09a52,#7a5a44)"></div><span>BARCELONA</span></div>
    <div class="event"><div class="event-photo" role="img" aria-label="Dark gym with dumbbell racks" style="background:linear-gradient(180deg,#4a4a50,#1e1e22)"></div><span>BARCELONA</span></div>
  </div>
</section>

<footer class="site-footer">
  <div class="brand foot-brand"><span class="brand-dot"></span>LiftHarbor</div>
  <div class="foot-col info">
    <h4>More Info:</h4>
    <ul>
      <li><svg width="14" height="16" viewBox="0 0 14 16"><path d="M7 0a5 5 0 0 0-5 5c0 4 5 11 5 11s5-7 5-11a5 5 0 0 0-5-5z" fill="#ddd"/><circle cx="7" cy="5" r="2" fill="#050505"/></svg><span>LiftHarbor<br>100 Harbor Lane, Millbrook,<br>SC 29000.</span></li>
      <li><svg width="14" height="14" viewBox="0 0 14 14"><path d="M3 1l2 3-1.5 1.5a8 8 0 0 0 5 5L10 9l3 2-1 2.5C6 13 1 8 .5 2z" fill="#ddd"/></svg><span>0100 555 0199</span></li>
      <li><svg width="14" height="12" viewBox="0 0 14 12"><rect x="0" y="1" width="14" height="10" fill="#ddd"/><path d="M0 1l7 5 7-5" stroke="#050505" fill="none"/></svg><span>info@liftharbor.example</span></li>
    </ul>
  </div>
  <div class="foot-col links">
    <h4>Quick Links:</h4>
    <ul><li>HOME</li><li>LISTINGS</li><li>FEATURES</li><li>PAGES</li><li>LOG IN</li></ul>
  </div>
  <div class="foot-col signup">
    <h4>Newsletter Signup</h4>
    <div class="field">Email Address</div>
    <div class="submit">SUBMIT</div>
  </div>
  <div class="foot-rule"></div>
  <p class="copyright">Copyright © 2018.LiftHarbor . All rights reserved.</p>
  <div class="social"><i></i><i></i><i></i><i></i></div>
</footer>

</body>
</html>
```